Consulting firm needs elegant, modern designs

Business card design - I have a logo which has previously been developed for Q-Pathways - I will attach. I will also attach specifications for the size of the business card.

We also need a logo design for our leadership consulting product - Form in Guidance - we focus on improving workplace health by educating leaders and learning professionals about how the physical and emotional affects performance and engagement. I have some example logos and ideas which I will attach - these have attempted to bring in the body but I do not like the font (see www.formingguidance-example.com for preferred font). Idea is to please have a 'body' visible somehow in the word Leadership, ensuring that this conveys flexibility and agility. Colors which I prefer are deep purple OR turquoise, together with silver. COLORS below are for LOGO design.

Target Market(s)

For the business card, it should be more masculine. The logo which will be attached should be neutralized into dark blue shades and silver. The business card Q-Pathways is focused on business transformation - organizations who would require a consultant to help them enter new markets, for example.

Industry/Entity Type

Leadership

Contact Information for Business Card

Content:
Q-Pathways
Lindenkade 27
4921KP, Havenmeer, The Netherlands
maurits@Q-Pathways.example
www.Q-Pathways.example

Colors for business card should be conservative and slightly more masculine. Use the Q-Pathways logo but change the colors to blue or shades of gray/black.

Dimensions for cut
85 x 55 mm
1004 x 650 pixels
Full document size
88 x 58 mm
1040 x 685 pixels
For the best result, you need to design the full document size including the bleed

Logo Text

Form in Guidance

Font styles to use
Serif
Sans Serif

Colors
876aae
333333
959595

Requirements
Must have
• Professional, modern and unique business card design
• Professional, elegant, and modern logo design - with creative thinking
Should not have
• Too many colors

```html
<!DOCTYPE html>
<html lang="en">
<head>
<meta charset="utf-8">
<title>Q-Pathways business card</title>
<link rel="stylesheet" href="https://fonts.googleapis.com/css2?family=Source+Sans+3:wght@300;400;600&display=swap">
<style>
  :root {
    --ink: #22183f;
    --paper: #ffffff;
    --line: #111111;
    --teal: #1a7f9b;
    --muted: #5a5a5a;
  }
  html, body {
    margin: 0;
    padding: 0;
    width: 880px;
    height: 1200px;
    overflow: hidden;
    background: var(--paper);
    font-family: "Source Sans 3", sans-serif;
  }
  .sheet {
    position: relative;
    width: 880px;
    height: 1200px;
  }
  .card {
    position: absolute;
    left: 68px;
    width: 746px;
    height: 482px;
    box-sizing: border-box;
  }
  .card--front {
    top: 86px;
    background: var(--ink);
    border-top-right-radius: 60px;
  }
  .card--back {
    top: 632px;
    background: var(--paper);
    border: 1.5px solid var(--line);
    border-top-left-radius: 60px;
  }
  .front-brand {
    position: absolute;
    left: 0;
    right: 0;
    top: 168px;
    text-align: center;
    color: var(--paper);
    font-weight: 600;
    font-size: 60px;
    letter-spacing: 0.5px;
  }
  .front-url {
    position: absolute;
    left: 0;
    right: 0;
    top: 402px;
    text-align: center;
    color: var(--paper);
    font-weight: 300;
    font-size: 25px;
  }
  .brand {
    position: absolute;
    left: 222px;
    top: 80px;
    display: flex;
    align-items: center;
    gap: 16px;
  }
  .brand-dot {
    width: 40px;
    height: 40px;
    border-radius: 50%;
    background: var(--teal);
  }
  .brand-name {
    color: var(--ink);
    font-weight: 600;
    font-size: 56px;
    line-height: 1;
  }
  .tagline {
    position: absolute;
    left: 366px;
    top: 154px;
    color: var(--muted);
    font-weight: 300;
    font-size: 21px;
    letter-spacing: 0.3px;
  }
  .contact-panel {
    position: absolute;
    left: 221px;
    right: -1.5px;
    top: 228px;
    height: 184px;
    background: var(--ink);
    border-top-left-radius: 24px;
  }
  .contact-row {
    position: absolute;
    right: 24px;
    display: flex;
    align-items: center;
    gap: 24px;
    color: var(--paper);
    font-weight: 300;
    font-size: 29px;
    line-height: 37px;
    text-align: right;
  }
  .contact-row--address { top: 22px; }
  .contact-row--email { top: 124px; }
  .contact-icon {
    width: 36px;
    height: 36px;
    flex: none;
  }
</style>
</head>
<body>
<div class="sheet">
  <section class="card card--front">
    <div class="front-brand">Q-Pathways</div>
    <div class="front-url">www.Q-Pathways.example</div>
  </section>

  <section class="card card--back">
    <div class="brand">
      <span class="brand-dot"></span>
      <span class="brand-name">Q-Pathways</span>
    </div>
    <div class="tagline">Supporting every stride</div>

    <div class="contact-panel">
      <div class="contact-row contact-row--address">
        <div>Lindenkade 27<br>4921KP, Havenmeer, The Netherlands</div>
        <svg class="contact-icon" viewBox="0 0 36 36" aria-hidden="true">
          <circle cx="18" cy="18" r="16" fill="#ffffff" stroke="#1a7f9b" stroke-width="3"/>
          <path d="M18 8.5c-4 0-6.8 3-6.8 6.7 0 4.6 6.8 12 6.8 12s6.8-7.4 6.8-12c0-3.7-2.8-6.7-6.8-6.7z" fill="#22183f"/>
          <circle cx="18" cy="15.2" r="2.6" fill="#ffffff"/>
        </svg>
      </div>
      <div class="contact-row contact-row--email">
        <div>maurits@Q-Pathways.example</div>
        <svg class="contact-icon" viewBox="0 0 36 36" aria-hidden="true">
          <circle cx="18" cy="18" r="16" fill="#ffffff" stroke="#1a7f9b" stroke-width="3"/>
          <rect x="10" y="12.5" width="16" height="11" rx="1" fill="#22183f"/>
          <path d="M10.5 13.2 18 19l7.5-5.8" fill="none" stroke="#ffffff" stroke-width="1.2"/>
        </svg>
      </div>
    </div>
  </section>
</div>
</body>
</html>
```